Vexor Mind Social Media Advertisement

We need a social media advertisement made up for our Asset Insight. Our initial campaign will be on Reddit, so it needs to be compliant with reddit. Attached is a brief, we just need 1 single design initially that we can interchange the copy to see what converts better. Must be in a format that we can easily edit. Attached also are some examples of advertisements that are currently posted on Reddit for similar products. Coinsprig is the closest competitor. Please visit our website: https://www.vexormind.example to understand more about the business. You can also register as a free user to view the platform.

Target Market(s)

Self-directed Australian investors — particularly Self managed super fund trustees and property investors — who actively manage their own wealth and want AI-powered insights to make smarter financial decisions.

Industry/Entity Type

Financial technology (FinTech) / Wealth management software.

Requirements
Must have
• Dark, sophisticated colour palette (navy and teal), no emoji or decorative icons, clean and modern typography, and imagery that conveys intelligence, data, and financial confidence — not generic stock market clichés.
Nice to have
• Subtle futuristic or tech aesthetic, data visualisation elements (charts, graphs, network nodes), a sense of calm authority rather than aggressive "get rich" energy, and designs that would work across both digital ads and print formats.
Should not have
• Bright or garish colours, cartoonish illustrations, generic stock market imagery (bulls, bears, ticker tape), cluttered layouts, anything that feels salesy or hype-driven, and no cryptocurrency or "get rich quick" visual cues.

```html
<!DOCTYPE html>
<html lang="en">
<head>
<meta charset="utf-8">
<title>Vexor Mind — Retirement Planning Ad Set</title>
<link href="https://fonts.googleapis.com/css2?family=Inter:wght@600;700;800&family=Figtree:wght@400;500;700&display=swap" rel="stylesheet">
<style>
  :root {
    --navy: #0f1b2e;
    --navy-deep: #0b1424;
    --navy-shape: #0d1829;
    --panel: #0c1626;
    --field: #13243e;
    --teal: #2dd5c4;
    --teal-light: #6ff0dc;
    --white: #ffffff;
    --ink-dark: #0a1a22;
    --page: #ffffff;
  }
  * { box-sizing: border-box; margin: 0; padding: 0; }
  html, body { width: 1200px; height: 724px; overflow: hidden; background: var(--page); }
  body { position: relative; font-family: "Figtree", Arial, sans-serif; }

  .ad { position: absolute; background: var(--navy); overflow: hidden; }
  .abs { position: absolute; }

  .headline {
    font-family: "Inter", Arial, sans-serif; font-weight: 800;
    letter-spacing: -0.045em; white-space: nowrap; color: var(--white);
  }
  .headline--teal { color: var(--teal); }

  .body-copy { color: var(--white); white-space: nowrap; }
  .body-copy strong { font-weight: 700; }

  .cta {
    border-radius: 999px; display: flex; align-items: center; justify-content: center;
    background: linear-gradient(90deg, var(--teal-light), var(--teal));
    color: var(--ink-dark); font-weight: 700; font-family: "Inter", Arial, sans-serif;
    letter-spacing: -0.01em; white-space: nowrap;
  }
  .brand-name {
    font-family: "Inter", Arial, sans-serif; font-weight: 700; color: var(--white);
    letter-spacing: -0.03em; white-space: nowrap;
  }
  .site-url { color: var(--white); white-space: nowrap; text-align: right; }

  .planner {
    position: absolute; width: 229px; height: 273px; background: var(--panel);
    transform-origin: 0 0; font-family: "Figtree", Arial, sans-serif;
  }
  .planner__label { position: absolute; color: var(--teal); font-size: 10px; font-weight: 500; white-space: nowrap; }
  .planner__select {
    position: absolute; height: 27px; background: var(--field); border-radius: 2px;
    display: flex; align-items: center; gap: 8px; padding-left: 10px; color: var(--teal); font-size: 9.5px;
  }
  .planner__select svg { flex: none; }
  .planner__select .chev { margin-left: auto; margin-right: 12px; }
  .planner__button {
    position: absolute; height: 28px; background: var(--teal); border-radius: 2px;
    display: flex; align-items: center; justify-content: center; color: var(--ink-dark); font-size: 10px; font-weight: 500;
  }
  .planner__textarea { position: absolute; background: var(--field); border-radius: 2px; }

  .side-dark { position: absolute; top: 0; bottom: 0; background: var(--navy-deep); }
</style>
</head>
<body>

<!-- Square format -->
<section class="ad ad--square" style="left:46px; top:29px; width:664px; height:664px;">
  <svg class="abs" style="left:0;top:0" width="664" height="664" aria-hidden="true">
    <polygon points="379,154 664,229 664,664 354,664 222,620" fill="var(--navy-shape)"/>
  </svg>
  <div class="abs headline" style="left:42px; top:54px; font-size:46px; line-height:46px;">See exactly when<br>you can retire.</div>
  <div class="abs headline headline--teal" style="left:42px; top:161px; font-size:46px; line-height:48px;">Then build the<br>path to get there.</div>
  <div class="abs site-url" style="right:37px; top:70px; font-size:13px;">vexormind.example</div>
  <div class="abs" style="left:656px; top:62px; width:8px; height:33px; background:var(--teal);"></div>

  <div class="abs body-copy" style="left:45px; top:378px; font-size:19px; line-height:22px; letter-spacing:0.01em;">Your retirement date<br>isn’t a guess.</div>
  <div class="abs body-copy" style="left:45px; top:422px; font-size:21px; line-height:25px;"><strong>Model it, track it,<br>own it.</strong></div>

  <div class="abs cta" style="left:49px; top:548px; width:163px; height:36px; font-size:16px;">Start Free Trial</div>

  <div class="planner" style="left:382px; top:301px;">
    <div class="planner__label" style="left:30px; top:17px;">Select Retirement Date And Year</div>
    <div class="planner__select" style="left:30px; top:35px; width:79px;">
      <svg width="12" height="12" viewBox="0 0 12 12" fill="none" stroke="var(--teal)" stroke-width="1"><rect x="1" y="2" width="10" height="9" rx="1"/><line x1="1" y1="5" x2="11" y2="5"/><line x1="4" y1="0.5" x2="4" y2="3"/><line x1="8" y1="0.5" x2="8" y2="3"/></svg>
      Date<svg class="chev" width="7" height="5" viewBox="0 0 7 5" fill="none" stroke="var(--teal)" stroke-width="1.2"><polyline points="1,1 3.5,3.5 6,1"/></svg>
    </div>
    <div class="planner__select" style="left:117px; top:35px; width:77px;">
      <svg width="12" height="12" viewBox="0 0 12 12" fill="none" stroke="var(--teal)" stroke-width="1"><rect x="1" y="2" width="10" height="9" rx="1"/><line x1="1" y1="5" x2="11" y2="5"/><line x1="4" y1="0.5" x2="4" y2="3"/><line x1="8" y1="0.5" x2="8" y2="3"/></svg>
      Year<svg class="chev" width="7" height="5" viewBox="0 0 7 5" fill="none" stroke="var(--teal)" stroke-width="1.2"><polyline points="1,1 3.5,3.5 6,1"/></svg>
    </div>
    <div class="planner__button" style="left:30px; top:71px; width:164px;">Confirm</div>
    <div class="planner__label" style="left:31px; top:116px;">Enter Your Plan Here</div>
    <div class="planner__textarea" style="left:31px; top:136px; width:165px; height:65px;"></div>
    <div class="planner__button" style="left:31px; top:216px; width:165px;">Build Plan</div>
  </div>

  <div class="abs brand-name" style="left:440px; top:584px; font-size:25px;">Vexor Mind</div>
</section>

<!-- Landscape format, copy variant A -->
<section class="ad ad--landscape" style="left:728px; top:29px; width:401px; height:210px;">
  <div class="side-dark" style="left:215px; right:0;"></div>
  <div class="abs headline" style="left:21px; top:18px; font-size:21px; line-height:21px;">See exactly when<br>you can retire.</div>
  <div class="abs headline headline--teal" style="left:21px; top:64px; font-size:21px; line-height:21px;">Then build the<br>path to get there.</div>
  <div class="abs body-copy" style="left:22px; top:126px; font-size:9px; line-height:11px;">Your retirement date isn’t a guess.<br><strong>Model it, track it, own it.</strong></div>
  <div class="abs cta" style="left:22px; top:173px; width:72px; height:15px; font-size:7.5px;">Start Free Trial</div>
  <div class="abs brand-name" style="left:148px; top:174px; font-size:10px;">Vexor Mind</div>
  <div class="planner" style="left:248px; top:24px; transform:scale(0.528);">
    <div class="planner__label" style="left:30px; top:17px;">Select Retirement Date And Year</div>
    <div class="planner__select" style="left:30px; top:35px; width:79px;"><svg width="12" height="12" viewBox="0 0 12 12" fill="none" stroke="var(--teal)" stroke-width="1"><rect x="1" y="2" width="10" height="9" rx="1"/><line x1="1" y1="5" x2="11" y2="5"/></svg>Date<svg class="chev" width="7" height="5" viewBox="0 0 7 5" fill="none" stroke="var(--teal)" stroke-width="1.2"><polyline points="1,1 3.5,3.5 6,1"/></svg></div>
    <div class="planner__select" style="left:117px; top:35px; width:77px;"><svg width="12" height="12" viewBox="0 0 12 12" fill="none" stroke="var(--teal)" stroke-width="1"><rect x="1" y="2" width="10" height="9" rx="1"/><line x1="1" y1="5" x2="11" y2="5"/></svg>Year<svg class="chev" width="7" height="5" viewBox="0 0 7 5" fill="none" stroke="var(--teal)" stroke-width="1.2"><polyline points="1,1 3.5,3.5 6,1"/></svg></div>
    <div class="planner__button" style="left:30px; top:71px; width:164px;">Confirm</div>
    <div class="planner__label" style="left:31px; top:116px;">Enter Your Plan Here</div>
    <div class="planner__textarea" style="left:31px; top:136px; width:165px; height:65px;"></div>
    <div class="planner__button" style="left:31px; top:216px; width:165px;">Build Plan</div>
  </div>
  <div class="abs site-url" style="right:26px; top:185px; font-size:5px;">vexormind.example</div>
</section>

<!-- Landscape format, copy variant B (mirrored layout) -->
<section class="ad ad--landscape" style="left:728px; top:256px; width:401px; height:210px;">
  <div class="side-dark" style="left:0; width:184px;"></div>
  <div class="planner" style="left:27px; top:28px; transform:scale(0.56);">
    <div class="planner__label" style="left:30px; top:17px;">Select Retirement Date And Year</div>
    <div class="planner__select" style="left:30px; top:35px; width:79px;"><svg width="12" height="12" viewBox="0 0 12 12" fill="none" stroke="var(--teal)" stroke-width="1"><rect x="1" y="2" width="10" height="9" rx="1"/><line x1="1" y1="5" x2="11" y2="5"/></svg>Date<svg class="chev" width="7" height="5" viewBox="0 0 7 5" fill="none" stroke="var(--teal)" stroke-width="1.2"><polyline points="1,1 3.5,3.5 6,1"/></svg></div>
    <div class="planner__select" style="left:117px; top:35px; width:77px;"><svg width="12" height="12" viewBox="0 0 12 12" fill="none" stroke="var(--teal)" stroke-width="1"><rect x="1" y="2" width="10" height="9" rx="1"/><line x1="1" y1="5" x2="11" y2="5"/></svg>Year<svg class="chev" width="7" height="5" viewBox="0 0 7 5" fill="none" stroke="var(--teal)" stroke-width="1.2"><polyline points="1,1 3.5,3.5 6,1"/></svg></div>
    <div class="planner__button" style="left:30px; top:71px; width:164px;">Confirm</div>
    <div class="planner__label" style="left:31px; top:116px;">Enter Your Plan Here</div>
    <div class="planner__textarea" style="left:31px; top:136px; width:165px; height:65px;"></div>
    <div class="planner__button" style="left:31px; top:216px; width:165px;">Build Plan</div>
  </div>
  <div class="abs headline" style="left:207px; top:18px; font-size:21px; line-height:21px;">See exactly when<br>you can retire.</div>
  <div class="abs headline headline--teal" style="left:207px; top:64px; font-size:21px; line-height:21px;">Then build the<br>path to get there.</div>
  <div class="abs body-copy" style="left:208px; top:126px; font-size:10px; line-height:11px;">Know your <strong>number</strong>. Know your<br><strong>date</strong>. Know your <strong>path</strong>.</div>
  <div class="abs brand-name" style="left:207px; top:170px; font-size:10px;">Vexor Mind</div>
  <div class="abs cta" style="left:302px; top:168px; width:72px; height:15px; font-size:7.5px;">Start Free Trial</div>
  <div class="abs site-url" style="right:27px; top:187px; font-size:5px;">vexormind.example</div>
</section>

<!-- Landscape format, copy variant C -->
<section class="ad ad--landscape" style="left:728px; top:483px; width:401px; height:210px;">
  <div class="side-dark" style="left:215px; right:0;"></div>
  <div class="abs headline" style="left:21px; top:18px; font-size:21px; line-height:21px;">See exactly when<br>you can retire.</div>
  <div class="abs headline headline--teal" style="left:21px; top:64px; font-size:21px; line-height:21px;">Then build the<br>path to get there.</div>
  <div class="abs body-copy" style="left:22px; top:126px; font-size:9px; line-height:11px;">Your retirement date isn’t a guess.<br><strong>Model it, track it, own it.</strong></div>
  <div class="abs cta" style="left:22px; top:173px; width:72px; height:15px; font-size:7.5px;">Start Free Trial</div>
  <div class="abs brand-name" style="left:148px; top:174px; font-size:10px;">Vexor Mind</div>
  <div class="planner" style="left:248px; top:24px; transform:scale(0.528);">
    <div class="planner__label" style="left:30px; top:17px;">Select Retirement Date And Year</div>
    <div class="planner__select" style="left:30px; top:35px; width:79px;"><svg width="12" height="12" viewBox="0 0 12 12" fill="none" stroke="var(--teal)" stroke-width="1"><rect x="1" y="2" width="10" height="9" rx="1"/><line x1="1" y1="5" x2="11" y2="5"/></svg>Date<svg class="chev" width="7" height="5" viewBox="0 0 7 5" fill="none" stroke="var(--teal)" stroke-width="1.2"><polyline points="1,1 3.5,3.5 6,1"/></svg></div>
    <div class="planner__select" style="left:117px; top:35px; width:77px;"><svg width="12" height="12" viewBox="0 0 12 12" fill="none" stroke="var(--teal)" stroke-width="1"><rect x="1" y="2" width="10" height="9" rx="1"/><line x1="1" y1="5" x2="11" y2="5"/></svg>Year<svg class="chev" width="7" height="5" viewBox="0 0 7 5" fill="none" stroke="var(--teal)" stroke-width="1.2"><polyline points="1,1 3.5,3.5 6,1"/></svg></div>
    <div class="planner__button" style="left:30px; top:71px; width:164px;">Confirm</div>
    <div class="planner__label" style="left:31px; top:116px;">Enter Your Plan Here</div>
    <div class="planner__textarea" style="left:31px; top:136px; width:165px; height:65px;"></div>
    <div class="planner__button" style="left:31px; top:216px; width:165px;">Build Plan</div>
  </div>
  <div class="abs site-url" style="right:26px; top:185px; font-size:5px;">vexormind.example</div>
</section>

</body>
</html>
```